Scrap Metal Recycling

We are looking for a simple yet bold business card. We already have the logo, please see attached. Color scheme of blue, black and white or just blue and white.

```html
<!DOCTYPE html>
<html lang="en">
<head>
<meta charset="utf-8">
<title>Ridgeline Metals Inc. – Business Card</title>
<link rel="stylesheet" href="https://fonts.googleapis.com/css2?family=Montserrat:wght@400;600;700&display=swap">
<style>
  :root {
    --bg: #d8d8d8;
    --paper: #f1f1ef;
    --ink: #2b2b2b;
    --ink-soft: #5a5a5a;
    --blue: #1e9cc6;
    --edge: #1a94bf;
    --rule: #c9c9c6;
  }
  * { box-sizing: border-box; margin: 0; padding: 0; }
  html, body { width: 1200px; height: 1051px; overflow: hidden; }
  body {
    background: var(--bg);
    font-family: "Montserrat", Arial, sans-serif;
    display: flex;
    flex-direction: column;
    align-items: center;
    justify-content: center;
    gap: 51px;
  }
  .card {
    width: 700px;
    height: 400px;
    background: var(--paper);
    border-bottom: 6px solid var(--edge);
    box-shadow: 0 14px 30px rgba(0,0,0,0.18);
    position: relative;
  }
  .brand { display: flex; flex-direction: column; align-items: flex-start; }
  .brand-row { display: flex; align-items: center; gap: 14px; }
  .brand-dot { border-radius: 50%; background: var(--blue); flex: none; }
  .brand-name { font-weight: 700; color: var(--ink); white-space: nowrap; letter-spacing: 0.5px; }
  .brand-tagline { color: var(--blue); font-weight: 600; letter-spacing: 6px; text-transform: uppercase; white-space: nowrap; }

  /* front */
  .card-front { display: flex; align-items: center; justify-content: center; }
  .card-front .brand-dot { width: 30px; height: 30px; }
  .card-front .brand-name { font-size: 44px; }
  .card-front .brand-tagline { font-size: 18px; margin: 10px 0 0 44px; }

  /* back */
  .card-back { display: flex; align-items: center; padding: 0 32px; }
  .card-back .brand { flex: 0 0 330px; }
  .card-back .brand-row { gap: 12px; }
  .card-back .brand-dot { width: 16px; height: 16px; }
  .card-back .brand-name { font-size: 20px; }
  .card-back .brand-tagline { font-size: 10px; letter-spacing: 4px; margin: 7px 0 0 28px; }
  .divider { flex: none; width: 1px; height: 190px; background: var(--rule); margin: 0 24px 0 10px; }
  .contact { flex: 1; min-width: 0; color: var(--ink-soft); font-size: 15px; line-height: 1.45; }
  .contact-name { color: var(--blue); font-weight: 700; font-size: 22px; letter-spacing: 0.5px; white-space: nowrap; }
  .contact-role { margin-bottom: 10px; }
  .contact-address { margin-bottom: 8px; }
  .contact-line { display: flex; align-items: center; gap: 8px; white-space: nowrap; }
  .contact-line svg { width: 13px; height: 13px; fill: var(--blue); flex: none; }
</style>
</head>
<body>
  <section class="card card-front">
    <div class="brand">
      <div class="brand-row">
        <span class="brand-dot"></span>
        <span class="brand-name">RIDGELINE METALS INC.</span>
      </div>
      <span class="brand-tagline">Scrap Metal Recycling</span>
    </div>
  </section>

  <section class="card card-back">
    <div class="brand">
      <div class="brand-row">
        <span class="brand-dot"></span>
        <span class="brand-name">RIDGELINE METALS INC.</span>
      </div>
      <span class="brand-tagline">Scrap Metal Recycling</span>
    </div>
    <div class="divider"></div>
    <div class="contact">
      <p class="contact-name">MARK DELANEY</p>
      <p class="contact-role">President</p>
      <p class="contact-address">1180 Harbor View Road<br>Seacliff CA 90000</p>
      <p class="contact-line">
        <svg viewBox="0 0 24 24" aria-hidden="true"><path d="M6.6 10.8a15.1 15.1 0 0 0 6.6 6.6l2.2-2.2a1 1 0 0 1 1-.25 11.4 11.4 0 0 0 3.6.57 1 1 0 0 1 1 1V20a1 1 0 0 1-1 1A17 17 0 0 1 3 4a1 1 0 0 1 1-1h3.5a1 1 0 0 1 1 1c0 1.25.2 2.450.57 3.57a1 1 0 0 1-.25 1z"/></svg>
        555-014-2297
      </p>
      <p class="contact-line">
        <svg viewBox="0 0 24 24" aria-hidden="true"><path d="M2 5h20v14H2z M2 5l10 8 10-8"/></svg>
        mark@ridgelinemetals.com
      </p>
      <p class="contact-line">
        <svg viewBox="0 0 24 24" aria-hidden="true"><circle cx="12" cy="12" r="10"/></svg>
        www.ridgelinemetals.com
      </p>
    </div>
  </section>
</body>
</html>
```